Pre school dance flyer & Whole Dance Academy Flyer

to design a double sided flyer

one side for pre school pupils aged 18 months to five years

the other side a general whole Academy flyer

We are a dance and Performing Arts Academy

Reason: I've been very busy at work to focus on this

Target Market(s)

Pre school one side
school age to adult other side
Target is Pre school children side one - school age to adult the other

Industry/Entity Type

School

Font styles to use
Sans Serif

Requirements
Must have
• bright colourful and exciting
Should not have
• dark colours

```html
<!DOCTYPE html>
<html lang="en">
<head>
<meta charset="utf-8">
<title>Brightstep Dance Academy Flyers</title>
<link href="https://fonts.googleapis.com/css2?family=Great+Vibes&family=Marcellus+SC&family=Open+Sans:wght@400;600&display=swap" rel="stylesheet">
<style>
  :root {
    --pink: #e2388a;
    --cyan: #16c1ea;
    --teal: #1aa3c7;
    --white: #ffffff;
    --paper: #f3f3f3;
    --ink: #1c1c1c;
    --stage: #efeae4;
    --purple: #5b2a8e;
  }
  * { margin: 0; padding: 0; box-sizing: border-box; }
  html, body { width: 1200px; height: 1121px; overflow: hidden; }
  body { background: var(--stage); font-family: "Open Sans", sans-serif; position: relative; }

  .flyer {
    position: absolute; top: 160px; width: 532px; height: 746px;
    background: linear-gradient(180deg, var(--white), var(--paper));
    overflow: hidden; box-shadow: 0 6px 18px rgba(0,0,0,.18);
  }
  .flyer--trial { left: 37px; }
  .flyer--academy { left: 632px; }
  .flyer .shapes { position: absolute; inset: 0; }
  .abs { position: absolute; }

  .script { font-family: "Great Vibes", cursive; font-weight: 400; }
  .caps { font-family: "Marcellus SC", serif; }

  .brand { display: flex; align-items: center; gap: 5px; font-family: "Open Sans", sans-serif; font-weight: 600; font-size: 19px; color: var(--ink); white-space: nowrap; }
  .brand-dot { width: 11px; height: 11px; border-radius: 50%; background: var(--pink); }

  .trial-title { top: 290px; left: 0; width: 532px; text-align: center; font-size: 82px; color: var(--pink); line-height: 1; white-space: nowrap; }
  .trial-band-text { top: 374px; left: 0; width: 532px; text-align: center; font-size: 25px; color: var(--white); letter-spacing: 1px; text-transform: uppercase; line-height: 1.2; }

  .photo-circle { top: 428px; width: 144px; height: 144px; border-radius: 50%; border: 5px solid var(--white); box-shadow: 0 6px 10px rgba(0,0,0,.25); }
  .photo-circle--one { left: 27px; background: radial-gradient(circle at 40% 40%, #e8464b, #8a1430); }
  .photo-circle--two { left: 184px; width: 168px; height: 168px; top: 414px; background: linear-gradient(180deg, #2a5fa8 0%, #3b86c8 55%, #e4d9cf 80%, #b58a5c 100%); }
  .photo-circle--three { left: 363px; background: radial-gradient(circle at 50% 50%, #f06070, #b81c2d); }

  .trial-tagline { top: 590px; left: 30px; width: 472px; text-align: center; color: var(--white); font-size: 15.5px; font-weight: 600; line-height: 1.35; }

  .join-badge {
    border-radius: 50%; background: radial-gradient(circle at 50% 40%, #1fc6ea, var(--teal));
    border: 4px solid var(--white); box-shadow: 0 4px 10px rgba(0,0,0,.25);
    color: var(--white); text-align: center; display: flex; flex-direction: column; justify-content: center;
  }
  .join-badge .script { font-size: 48px; line-height: .9; }
  .join-badge .caps { font-size: 15px; line-height: 1.05; }
  .flyer--trial .join-badge { left: 22px; top: 626px; width: 122px; height: 122px; }

  .contact { font-size: 15px; color: var(--ink); font-weight: 600; white-space: nowrap; }
  .contact .label { font-family: "Marcellus SC", serif; color: var(--pink); font-weight: 400; margin-right: 6px; font-size: 15px; }
  .contact .big { font-size: 22px; }
  .contact-phone { top: 654px; left: 158px; }
  .contact-web { top: 684px; left: 151px; }
  .contact-venue { top: 707px; left: 162px; }
  .contact-address { top: 732px; left: 222px; font-size: 8px; color: var(--ink); }

  .flyer--trial .brand { top: 38px; left: 414px; }

  .join-us { top: 276px; left: 0; width: 532px; text-align: center; font-size: 46px; color: var(--white); line-height: 1; }
  .academy-copy { top: 333px; left: 0; width: 532px; text-align: center; color: var(--white); font-size: 20.5px; line-height: 1.33; white-space: nowrap; }
  .academy-band-text { top: 436px; left: 0; width: 532px; text-align: center; font-size: 36px; color: var(--white); line-height: 1.2; }

  .flyer--academy .brand { top: 512px; left: 54px; font-size: 22px; }
  .partner-badge--council { top: 506px; left: 194px; width: 118px; height: 40px; background: linear-gradient(180deg, #222 0 45%, transparent 45% 60%, #bbb 60% 100%); }
  .partner-badge--drama { top: 502px; left: 342px; width: 130px; height: 40px; background: var(--purple); }

  .flyer--academy .join-badge { left: 56px; top: 584px; width: 136px; height: 136px; }
  .flyer--academy .join-badge .script { font-size: 54px; }
  .flyer--academy .join-badge .caps { font-size: 16px; }

  .welcome { top: 588px; left: 198px; width: 310px; text-align: center; color: var(--teal); font-size: 27px; line-height: 1.1; }
  .flyer--academy .contact-phone { top: 652px; left: 229px; }
  .flyer--academy .contact-web { top: 680px; left: 223px; }
  .social { top: 706px; left: 237px; width: 280px; font-size: 13px; color: var(--ink); }
  .social span { position: absolute; top: 0; display: flex; align-items: center; gap: 5px; white-space: nowrap; }
  .social span:last-child { left: 185px; }
  .social i { width: 11px; height: 11px; background: #3b8fd6; display: inline-block; }
</style>
</head>
<body>

<section class="flyer flyer--trial">
  <svg class="shapes" viewBox="0 0 532 746" width="532" height="746">
    <defs>
      <linearGradient id="trialPhoto" x1="0" y1="0" x2="1" y2="1">
        <stop offset="0" stop-color="#3a2a2e"/>
        <stop offset=".5" stop-color="#7a3a3c"/>
        <stop offset="1" stop-color="#2a1c22"/>
      </linearGradient>
    </defs>
    <path d="M300,0 H322 Q380,20 532,180 V218 Q420,280 280,292 Q120,300 0,268 V220 Z" fill="var(--pink)"/>
    <path d="M0,0 H300 Q360,30 470,182 Q300,262 0,236 Z" fill="var(--cyan)"/>
    <path d="M0,268 Q120,300 280,292 Q420,280 532,218 V262 Q400,302 260,308 Q100,310 0,292 Z" fill="var(--cyan)"/>
    <path d="M0,20 Q200,-5 330,50 Q430,100 445,175 Q330,262 200,278 Q80,284 0,256 Z" fill="url(#trialPhoto)" role="img" aria-label="Photo of young dancers in cowgirl hats and red scarves performing on stage"/>
    <rect x="0" y="370" width="532" height="36" fill="var(--cyan)"/>
    <rect x="0" y="406" width="532" height="340" fill="var(--pink)"/>
    <path d="M0,660 Q200,620 532,636 V746 H0 Z" fill="var(--cyan)"/>
    <path d="M0,676 Q200,636 532,652 V746 H0 Z" fill="var(--paper)"/>
  </svg>

  <div class="abs brand"><span class="brand-dot"></span>Brightstep</div>

  <h1 class="abs trial-title script">Free Trial Class</h1>
  <p class="abs trial-band-text caps">For all new pupils</p>

  <div class="abs photo-circle photo-circle--one" role="img" aria-label="Photo of dancers in red costumes with parasols"></div>
  <div class="abs photo-circle photo-circle--two" role="img" aria-label="Photo of a ballet teacher with little dancers by a flower box"></div>
  <div class="abs photo-circle photo-circle--three" role="img" aria-label="Photo of dancers in red polka dot dresses lying on stage reading"></div>

  <p class="abs trial-tagline">Pursue a career in the Performing Arts or Simply attend for enjoyment and fun</p>

  <div class="abs join-badge">
    <span class="script">Join</span>
    <span class="caps">The Academy<br>Today</span>
  </div>

  <p class="abs contact contact-phone"><span class="label">Call us</span><span class="big">01632 960 418</span></p>
  <p class="abs contact contact-web"><span class="label">Website</span>www.brightstepdance.co.uk</p>
  <p class="abs contact contact-venue"><span class="label">Vanue</span>The Parish Hall of St Aldric</p>
  <p class="abs contact-address">Meadow Lane, Ashcombe, AB1 2CD</p>
</section>

<section class="flyer flyer--academy">
  <svg class="shapes" viewBox="0 0 532 746" width="532" height="746">
    <defs>
      <linearGradient id="academyPhoto" x1="0" y1="0" x2="0" y2="1">
        <stop offset="0" stop-color="#1d2a4a"/>
        <stop offset=".45" stop-color="#e9e4ec"/>
        <stop offset=".75" stop-color="#f07cbf"/>
        <stop offset="1" stop-color="#7ac7ee"/>
      </linearGradient>
    </defs>
    <rect x="0" y="0" width="532" height="434" fill="var(--pink)"/>
    <path d="M0,196 Q260,268 532,186 V212 Q260,290 0,222 Z" fill="var(--cyan)"/>
    <path d="M0,0 H532 V182 Q260,262 0,194 Z" fill="url(#academyPhoto)" role="img" aria-label="Photo of preschool ballerinas in white tops and colourful tutus on stage"/>
    <rect x="0" y="434" width="532" height="48" fill="var(--cyan)"/>
    <path d="M0,640 Q250,520 532,580 V590 Q250,540 0,660 Z" fill="var(--pink)"/>
    <path d="M0,660 Q250,540 532,590 V610 Q250,560 0,690 Z" fill="var(--cyan)"/>
    <path d="M0,690 Q250,560 532,610 V746 H0 Z" fill="var(--paper)"/>
  </svg>

  <h2 class="abs join-us script">Join Us</h2>
  <p class="abs academy-copy">Qualified dance teachers all DBS checked and<br>first aid trained, deliver an exciting curriculum which<br>is fun, stimulating and challenging.</p>
  <p class="abs academy-band-text script">Learn, Develop and Have Fun!</p>

  <div class="abs brand"><span class="brand-dot"></span>Brightstep</div>
  <div class="abs partner-badge--council" role="img" aria-label="Dance education council recognition badge"></div>
  <div class="abs partner-badge--drama" role="img" aria-label="Drama academy partner badge"></div>

  <div class="abs join-badge">
    <span class="script">Join</span>
    <span class="caps">The Academy<br>Today</span>
  </div>

  <p class="abs welcome caps">We Welcome<br>You to Straight</p>
  <p class="abs contact contact-phone"><span class="label">Call us</span><span class="big">01632 960 418</span></p>
  <p class="abs contact contact-web"><span class="label">Website</span>www.brightstepdance.co.uk</p>
  <div class="abs social">
    <span><i></i>@brightstepdance</span>
    <span><i></i>jmarlowarts</span>
  </div>
</section>

</body>
</html>
```